Halvern Capital, Inc.

We need a website design for a new company based in Orange County, CA but will be serving client's throughout all of California. We provide non-recourse loans/ pre-litigation funding for client's in personal injury and employment cases. Generally, if a client has an active case and they need money for cost of living, the client will contact a company like ours to provide a loan. We would like to see designs that are sleek, simple and easy to use. The final design should communicate trustworthiness, financial safety and promptness.

Hi, I like TK's designs. I am having him work on a hybrid of two of his designs. We had a little miscommunication, but we are almost there. Best, Ren

```html
<!DOCTYPE html>
<html lang="en">
<head>
<meta charset="utf-8">
<title>Halvern Capital Inc — Pre-Litigation Funding</title>
<link href="https://fonts.googleapis.com/css2?family=Open+Sans:wght@400;600;700;800&family=Nunito+Sans:wght@400;600;700&family=Montserrat:wght@800&display=swap" rel="stylesheet">
<style>
:root{
  --navy:#0b3175;
  --navy-deep:#092a66;
  --orange:#f47b20;
  --ink:#1d1d1d;
  --body:#444;
  --soft:#f3f1f1;
  --grey-band:#ebeaea;
  --form-grey:#6e6e6e;
  --footer:#232323;
  --white:#fff;
}
*{margin:0;padding:0;box-sizing:border-box}
html,body{width:1200px;height:3930px;overflow:hidden}
body{font-family:"Open Sans",sans-serif;color:var(--ink);background:var(--white)}
section,header,footer{position:relative;width:1200px}
.abs{position:absolute}
svg{display:block}

/* hero */
.hero{height:655px;background:var(--navy)}
.brand{left:131px;top:56px;color:var(--white);font-family:"Nunito Sans",sans-serif;font-weight:600;font-size:25px;letter-spacing:.3px}
.nav{left:450px;top:60px;display:flex;gap:34px;font-family:"Nunito Sans",sans-serif;font-size:15px;color:var(--white);letter-spacing:.3px}
.nav a{color:inherit;text-decoration:none;position:relative;padding-bottom:14px}
.nav a.active::after{content:"";position:absolute;left:0;right:0;bottom:0;height:3px;background:var(--white)}
.hero-title{left:0;width:1200px;top:245px;text-align:center;color:var(--white);font-family:"Nunito Sans",sans-serif;font-weight:600;line-height:1.2}
.hero-title .l1{font-size:33px;display:block}
.hero-title .l2{font-size:42px;display:block}
.hero-btn{left:503px;top:349px;width:182px;height:46px;border:2px solid var(--white);color:var(--white);font-family:"Nunito Sans",sans-serif;font-size:16px;display:flex;align-items:center;justify-content:center;letter-spacing:.5px}
.arrow{top:260px}

/* features */
.features{height:262px;background:var(--soft)}
.feature{top:30px;width:250px}
.feature h3{font-size:15px;font-weight:800;margin-top:14px}
.feature p{font-size:12px;line-height:1.4;color:var(--body);margin-top:6px}
.vline{top:40px;width:1px;height:180px;background:#cfcfcf}

/* steps */
.steps{height:629px}
.section-title{left:0;width:1200px;text-align:center;font-size:28px;font-weight:800;letter-spacing:.3px}
.title-rule{width:32px;height:2px;background:#888;left:584px}
.step{width:260px;text-align:center;top:370px}
.step h4{font-size:16px;font-weight:800}
.step p{font-size:15px;line-height:1.4;color:var(--body);margin-top:10px}
.btn-orange{background:var(--orange);color:var(--white);font-weight:800;display:flex;align-items:center;justify-content:center;letter-spacing:.4px}

/* funding */
.fund{height:660px;background:linear-gradient(180deg,#efeeee,#e6e5e5)}
.card{width:436px}
.card .photo{width:436px;height:312px;border:5px solid #d6d6d6}
.card h3{font-size:17px;font-weight:800;margin-top:28px;position:relative}
.card h3::before{content:"";position:absolute;left:0;top:-14px;width:62px;height:4px;background:var(--navy)}
.card p{font-size:14px;line-height:1.45;color:var(--body);margin-top:8px;width:380px}
.card .read{width:98px;height:26px;font-size:11px;margin-top:14px}

/* pre settlement */
.presettle{height:564px}
.ps-panel{left:144px;top:58px;width:283px;height:435px;background:#f3efee}
.ps-panel .rule{position:absolute;left:48px;top:90px;width:34px;height:3px;background:var(--orange)}
.ps-panel h3{position:absolute;left:48px;top:108px;width:200px;font-size:19px;font-weight:800;line-height:1.2}
.ps-panel p{position:absolute;left:48px;top:200px;width:200px;font-size:13px;line-height:1.4;color:var(--body)}
.ps-panel .read{position:absolute;left:48px;top:316px;width:94px;height:28px;font-size:11px}
.ps-photo{left:427px;top:58px;width:281px;height:435px;background:linear-gradient(180deg,#cfe3e0 0%,#9fc5bd 55%,#d9b99a 100%)}
.form-panel{left:728px;top:58px;width:333px;height:435px;background:var(--form-grey)}
.form-panel h3{position:absolute;left:28px;top:30px;color:var(--white);font-size:19px;font-weight:800;letter-spacing:.3px}
.field{position:absolute;left:32px;width:260px;height:30px;background:var(--white);font-size:11px;color:#777;padding:8px 10px;letter-spacing:.3px}
.form-panel .apply{position:absolute;left:32px;top:350px;width:260px;height:46px;font-size:16px}
.fold{left:1030px;top:2730px}

/* testimonials */
.testimonials{height:497px;background:#f3f1f1}
.quote{left:345px;width:510px;top:150px;text-align:center;font-size:15px;line-height:1.55;color:var(--body)}
.qmark{font-family:Georgia,serif;font-size:70px;color:#bdbdbd;line-height:1}
.avatar{width:76px;height:76px;border-radius:50%;top:330px;background:radial-gradient(circle at 50% 40%,#9b9b9b,#4a4a4a)}
.avatar.active{border:4px solid var(--orange);background:radial-gradient(circle at 50% 40%,#e6b48f,#b56c3e)}
.person{left:500px;width:200px;text-align:center;top:414px}
.person b{font-size:15px;font-weight:800;display:block}
.person span{font-size:12px;color:var(--body)}

/* cta */
.cta{height:270px;background:var(--navy)}
.cta h2{left:187px;top:74px;color:var(--white);font-size:29px;font-weight:800;line-height:1.2;letter-spacing:.3px}
.cta p{left:187px;top:170px;width:420px;color:#dbe3f2;font-size:15px;line-height:1.5}
.cta .enquiry{left:732px;top:73px;width:325px;height:50px;font-size:17px}
.cta .call{left:732px;top:148px;width:325px;height:50px;border:2px solid var(--white);color:var(--white);font-size:17px;display:flex;align-items:center;justify-content:center;font-weight:600}

/* footer */
.footer{height:393px;background:var(--footer);border-top:4px solid var(--orange);color:#e6e6e6}
.footer .logo{left:144px;top:118px;font-family:"Montserrat",sans-serif;font-weight:800;font-size:30px;color:var(--white)}
.fcol h5{font-size:13px;font-weight:700;color:var(--white);letter-spacing:.4px;margin-bottom:18px}
.fcol{font-size:12px;line-height:1.5}
.info-row{display:flex;gap:12px;margin-bottom:22px;align-items:flex-start}
.menu li{list-style:none;line-height:1.55;font-size:12px}
.social{display:flex;align-items:center;gap:12px;margin-bottom:14px}
.social i{width:24px;height:24px;border-radius:50%;display:block}
.footer .divider{left:487px;top:270px;width:570px;height:1px;background:#4a4a4a}
.footer .copy{left:478px;top:320px;font-size:12px;color:#cfcfcf}
</style>
</head>
<body>

<header class="hero">
  <div class="abs brand">HALVERN CAPITAL INC</div>
  <nav class="abs nav">
    <a class="active">HOME</a><a>ABOUT US</a><a>SERVICES</a><a>CAREERS</a><a>NEWS</a><a>CONTACT US</a>
  </nav>
  <svg class="abs arrow" style="left:110px" width="34" height="70" viewBox="0 0 34 70"><polyline points="30,4 4,35 30,66" fill="none" stroke="#fff" stroke-width="4"/></svg>
  <svg class="abs arrow" style="left:1056px" width="34" height="70" viewBox="0 0 34 70"><polyline points="4,4 30,35 4,66" fill="none" stroke="#fff" stroke-width="4"/></svg>
  <h1 class="abs hero-title"><span class="l1">WE PROVIDE NON-RECOURSE</span><span class="l2">LOANS/ PRE-LITIGATION FUNDING</span></h1>
  <div class="abs hero-btn">APPLY LOAN</div>
</header>

<section class="features">
  <div class="abs feature" style="left:144px">
    <svg width="58" height="80" viewBox="0 0 58 80"><path d="M29 4 L52 12 V36 C52 52 42 62 29 68 C16 62 6 52 6 36 V12 Z" fill="none" stroke="var(--navy)" stroke-width="5"/><text x="29" y="46" text-anchor="middle" font-family="Open Sans" font-weight="800" font-size="26" fill="var(--navy)">$</text><line x1="29" y1="70" x2="29" y2="78" stroke="var(--navy)" stroke-width="4"/><circle cx="29" cy="78" r="2" fill="var(--navy)"/></svg>
    <h3>RISK FREE</h3>
    <p>Lorem ipsum dolor sit amet consectetur adipiscing elit sed do eiusmod tempor incididunt ut labore.</p>
  </div>
  <div class="abs vline" style="left:425px"></div>
  <div class="abs feature" style="left:478px">
    <svg width="80" height="80" viewBox="0 0 80 80"><circle cx="48" cy="40" r="24" fill="var(--navy)"/><polyline points="48,26 48,40 58,46" fill="none" stroke="#fff" stroke-width="4"/><rect x="4" y="28" width="20" height="5" fill="var(--navy)"/><rect x="10" y="38" width="16" height="5" fill="var(--navy)"/><rect x="4" y="48" width="20" height="5" fill="var(--navy)"/></svg>
    <h3>FAST AND EASY</h3>
    <p>Lorem ipsum dolor sit amet consectetur adipiscing elit sed do eiusmod tempor incididunt ut labore.</p>
  </div>
  <div class="abs vline" style="left:757px"></div>
  <div class="abs feature" style="left:825px">
    <svg width="40" height="80" viewBox="0 0 40 80"><text x="20" y="62" text-anchor="middle" font-family="Open Sans" font-weight="800" font-size="64" fill="var(--navy)">$</text></svg>
    <h3>LOW RATES</h3>
    <p>Lorem ipsum dolor sit amet consectetur adipiscing elit sed do eiusmod tempor incididunt ut labore.</p>
  </div>
</section>

<section class="steps">
  <h2 class="abs section-title" style="top:55px">OUR 3 EASY STEPS</h2>
  <div class="abs title-rule" style="top:105px"></div>

  <svg class="abs" style="left:185px;top:140px" width="830" height="200" viewBox="0 0 830 200">
    <g fill="none" stroke="var(--orange)" stroke-width="2">
      <path d="M22 60 A92 92 0 0 1 200 60"/>
      <path d="M344 140 A92 92 0 0 0 520 140"/>
      <path d="M630 60 A92 92 0 0 1 806 60"/>
    </g>
    <g fill="var(--orange)">
      <polygon points="192,58 210,58 200,72"/>
      <polygon points="512,142 530,142 520,128"/>
      <polygon points="798,58 816,58 806,72"/>
    </g>
    <circle cx="112" cy="78" r="68" fill="var(--navy)"/>
    <circle cx="432" cy="78" r="68" fill="var(--navy)"/>
    <circle cx="718" cy="78" r="68" fill="var(--navy)"/>
    <path d="M92 62 c-6 6 -2 22 12 34 s26 16 32 10 l-8 -10 -8 4 c-6 -3 -14 -11 -16 -17 l4 -8 z" fill="#fff"/>
    <path d="M122 58 a14 14 0 0 1 12 12 M122 48 a24 24 0 0 1 22 22" fill="none" stroke="#fff" stroke-width="3"/>
    <path d="M418 94 l4 -14 28 -28 10 10 -28 28 z" fill="#fff"/><rect x="406" y="102" width="52" height="4" fill="#fff"/>
    <circle cx="718" cy="62" r="14" fill="#fff"/><text x="718" y="68" text-anchor="middle" font-family="Open Sans" font-weight="800" font-size="16" fill="var(--navy)">$</text>
    <path d="M690 92 l14 -6 h20 l16 -6 c4 0 5 4 2 6 l-18 12 h-34 z" fill="#fff"/>
    <circle cx="22" cy="60" r="14" fill="var(--orange)"/><text x="22" y="65" text-anchor="middle" font-family="Open Sans" font-weight="700" font-size="13" fill="#fff">01</text>
    <circle cx="344" cy="140" r="14" fill="var(--orange)"/><text x="344" y="145" text-anchor="middle" font-family="Open Sans" font-weight="700" font-size="13" fill="#fff">02</text>
    <circle cx="630" cy="60" r="14" fill="var(--orange)"/><text x="630" y="65" text-anchor="middle" font-family="Open Sans" font-weight="700" font-size="13" fill="#fff">03</text>
  </svg>

  <div class="abs step" style="left:167px"><h4>CALL US</h4><p>Apply online or call to speak<br>with a friendly agent</p></div>
  <div class="abs vline" style="left:447px;top:365px;height:90px"></div>
  <div class="abs step" style="left:470px"><h4>APPLY</h4><p>Lorem ipsum dolor sit amet<br>consectetur adipiscing.</p></div>
  <div class="abs vline" style="left:758px;top:365px;height:90px"></div>
  <div class="abs step" style="left:773px"><h4>GET PAID!</h4><p>Lorem ipsum dolor sit amet<br>consectetur adipiscing.</p></div>

  <div class="abs btn-orange" style="left:495px;top:511px;width:210px;height:44px;font-size:14px">GET STARTED NOW</div>
</section>

<section class="fund">
  <h2 class="abs section-title" style="top:48px">WHAT WE FUND</h2>
  <div class="abs title-rule" style="top:96px"></div>
  <div class="abs card" style="left:144px;top:147px">
    <div class="photo" role="img" aria-label="Injured construction worker kneeling at a building site" style="background:linear-gradient(180deg,#c9c3b8 0%,#a89a86 55%,#8a7560 100%)"></div>
    <h3>PERSONAL INJURY</h3>
    <p>Lorem ipsum dolor sit amet consectetur adipiscing elit sed do eiusmod tempor incididunt ut labor magna aliqua. Ut enim ad minim veniam.</p>
    <div class="btn-orange read">READ MORE</div>
  </div>
  <div class="abs card" style="left:620px;top:147px">
    <div class="photo" role="img" aria-label="Professional woman working on a laptop in a bright office" style="background:linear-gradient(180deg,#eeeeec 0%,#d9d7d3 60%,#b9b1a8 100%)"></div>
    <h3>EMPLOYMENT CASES</h3>
    <p>Lorem ipsum dolor sit amet consectetur adipiscing elit sed do eiusmod tempor incididunt ut labor magna aliqua. Ut enim ad minim veniam.</p>
    <div class="btn-orange read">READ MORE</div>
  </div>
</section>

<section class="presettle">
  <div class="abs ps-panel">
    <div class="rule"></div>
    <h3>PRE SETTLEMENT FUNDING FOR CLIENT'S</h3>
    <p>Lorem ipsum dolor sit amet consectetur adipiscing elit sed do eiusmod tempor incididunt ut labor magna aliqua. Ut enim ad minim veniam.</p>
    <div class="btn-orange read">READ MORE</div>
  </div>
  <div class="abs ps-photo" role="img" aria-label="Hand holding a small tree growing from stacked coins"></div>
  <svg class="abs" style="left:676px;top:462px" width="32" height="31" viewBox="0 0 32 31"><polygon points="32,0 32,31 0,31" fill="#fff"/><polygon points="32,0 0,31 14,4" fill="#cfcfcf"/></svg>
  <div class="abs form-panel">
    <h3>GET STARTED TODAY</h3>
    <div class="field" style="top:82px">NAME</div>
    <div class="field" style="top:124px">E-MAIL</div>
    <div class="field" style="top:166px">PHONE</div>
    <div class="field" style="top:208px;height:132px">MESSAGE</div>
    <div class="btn-orange apply">APPLY NOW</div>
  </div>
  <svg class="abs" style="left:1030px;top:462px" width="32" height="31" viewBox="0 0 32 31"><polygon points="32,0 32,31 0,31" fill="#fff"/><polygon points="32,0 0,31 14,4" fill="#bdbdbd"/></svg>
</section>

<section class="testimonials">
  <h2 class="abs section-title" style="top:52px">TESTIMONIALS</h2>
  <div class="abs title-rule" style="top:102px"></div>
  <div class="abs qmark" style="left:340px;top:118px">&ldquo;</div>
  <p class="abs quote">Lorem ipsum dolor sit amet consectetur adipiscing elit sed do eiusmod tempor incididunt ut labor magna aliqua. Ut enim ad minim veniam. Sed ut perspiciatis unde omnis iste natus error sit voluptatem accusantium doloremque laud antium, totam rem aperiam, eaque ipsa quae ab illo inventore veritatis et quasi architecto beatae vitae dicta sunt explicabo. Nemo enim ipsam quia.</p>
  <div class="abs qmark" style="left:778px;top:250px">&rdquo;</div>
  <svg class="abs" style="left:592px;top:308px" width="16" height="10" viewBox="0 0 16 10"><polygon points="8,0 16,10 0,10" fill="var(--navy)"/></svg>
  <div class="abs avatar" role="img" aria-label="Client portrait" style="left:345px"></div>
  <div class="abs avatar" role="img" aria-label="Client portrait" style="left:454px;background:radial-gradient(circle at 50% 40%,#c9c9c9,#8a8a8a)"></div>
  <div class="abs avatar active" role="img" aria-label="Portrait of Daniel" style="left:560px"></div>
  <div class="abs avatar" role="img" aria-label="Client portrait" style="left:672px"></div>
  <div class="abs avatar" role="img" aria-label="Client portrait" style="left:781px"></div>
  <div class="abs person"><b>DANIEL</b><span>San Diego</span></div>
  <div class="abs" style="left:572px;top:463px;width:56px;height:3px;background:var(--orange)"></div>
</section>

<section class="cta">
  <h2 class="abs">WE'RE HERE TO HELP.<br>MAKE AN ENQUIRY NOW</h2>
  <p class="abs">Lorem ipsum dolor sit amet consectetur adipiscing elit sed do eiusmod tempor incididunt ut labor magna aliqua.</p>
  <div class="abs btn-orange enquiry">MAKE AN ENQUIRY</div>
  <div class="abs call">Call us on 949.555.0142</div>
</section>

<footer class="footer">
  <div class="abs logo">Halvern Capital Inc</div>
  <div class="abs fcol" style="left:487px;top:58px;width:240px">
    <h5>CONTACT US</h5>
    <div class="info-row"><svg width="12" height="14" viewBox="0 0 12 14"><path d="M6 0a5 5 0 0 1 5 5c0 4-5 9-5 9S1 9 1 5a5 5 0 0 1 5-5z" fill="#ddd"/><circle cx="6" cy="5" r="2" fill="var(--footer)"/></svg><span>2150 Harbor Crest Way<br>Irvine, CA 92614</span></div>
    <div class="info-row"><svg width="12" height="12" viewBox="0 0 12 12"><path d="M2 1l3 2-1 2c1 2 2 3 3 3l2-1 2 3-2 2C4 12 0 8 0 3z" fill="#ddd"/></svg><span>949.555.0142</span></div>
    <div class="info-row"><svg width="14" height="11" viewBox="0 0 14 11"><rect width="14" height="11" fill="#ddd"/><polyline points="0,0 7,6 14,0" fill="none" stroke="var(--footer)" stroke-width="1.5"/></svg><span>info@halverncapital.com</span></div>
  </div>
  <div class="abs fcol" style="left:778px;top:58px">
    <h5>MENU</h5>
    <ul class="menu"><li>HOME</li><li>ABOUT US</li><li>WHAT WE FUND</li><li>HOW IT WORKS</li><li>BLOG</li><li>CONTACT US</li></ul>
  </div>
  <div class="abs fcol" style="left:943px;top:58px">
    <h5>CONNECT WITH US</h5>
    <div class="social"><i style="background:#3b5998"></i><span>Friendwall</span></div>
    <div class="social"><i style="background:#1da1f2"></i><span>Chirpline</span></div>
    <div class="social"><i style="background:#0e1e3d"></i><span>Workround</span></div>
  </div>
  <div class="abs divider"></div>
  <div class="abs copy">Copyright @ 2019 All Rights Reserved</div>
</footer>

</body>
</html>
```